Modern corporate energy/fuel business need business card design

Business card required for company founder. Korvan Fuels is a Australian based modern energy/fuel provider. We offer specialised solutions to businesses using fossil fuels through renewable energy solutions.

I would like one side with specific information (name, address etc)

The other side to be bold, professional company name & logo. Striking.

Target Market(s)

B2B. Transport, mining, councils, environmentalist,

Industry/Entity Type

Petroleum

Contact Information for Business Card

Name; Peter Morrow
Position; Director
Email; pmorrow@korvanse.com.au
Address; PO Box 347, Marlow Vale, NSW, 2790
Website; www.korvanse.com.au

Colors

Designer to choose colors to be used in the design.

Requirements
Must have
• Clean, easy to read, professional & strong theme
Should not have
• too many colours, busy layout,

```html
<!DOCTYPE html>
<html lang="en">
<head>
<meta charset="utf-8">
<title>Korvan Fuels — Business Card</title>
<link rel="stylesheet" href="https://fonts.googleapis.com/css2?family=Open+Sans:wght@400;600;700&display=swap">
<style>
  :root {
    --orange: #f58a33;
    --card: #ebeae6;
    --ink: #333333;
    --brand-grey: #5a5a5a;
    --page: #ffffff;
  }
  * { box-sizing: border-box; margin: 0; padding: 0; }
  html, body {
    width: 1200px; height: 1200px; overflow: hidden;
    background: var(--page);
    font-family: "Open Sans", Arial, sans-serif;
  }
  .canvas { position: relative; width: 1200px; height: 1200px; }

  .card {
    position: absolute;
    left: 186px;
    width: 828px;
    height: 496px;
    background: var(--card);
    overflow: hidden;
  }
  .card--front { top: 64px; }
  .card--back { top: 634px; }

  /* Front: brand */
  .brand {
    position: absolute; inset: 0;
    display: flex; flex-direction: column;
    align-items: center; justify-content: center;
    gap: 24px;
  }
  .brand__dot {
    width: 84px; height: 84px; border-radius: 50%;
    background: var(--orange);
  }
  .brand__name {
    font-weight: 600;
    font-size: 40px;
    letter-spacing: 6px;
    text-transform: uppercase;
    color: var(--brand-grey);
  }

  /* Back: name label */
  .name-tag {
    position: absolute;
    left: 78px; top: 99px;
    width: 296px; height: 106px;
    background: var(--orange);
    color: #fff;
    padding: 18px 26px;
    box-shadow: 0 14px 10px -8px rgba(245, 138, 51, 0.35);
  }
  .name-tag__name {
    font-size: 29px; line-height: 1.15;
    font-weight: 400; text-transform: uppercase;
    white-space: nowrap;
  }
  .name-tag__name strong { font-weight: 700; }
  .name-tag__role { font-size: 18px; margin-top: 4px; }

  /* Back: contacts */
  .contacts {
    position: absolute;
    left: 0; right: 0; top: 305px;
    height: 110px;
  }
  .contact {
    position: absolute; top: 0;
    width: 240px; margin-left: -120px;
    display: flex; flex-direction: column; align-items: center;
    text-align: center;
    color: var(--ink);
    font-size: 16px; line-height: 22px;
    letter-spacing: -0.2px;
    white-space: nowrap;
  }
  .contact svg { width: 40px; height: 40px; margin-bottom: 13px; }
  .contact--email { left: 182px; }
  .contact--web { left: 428px; }
  .contact--post { left: 656px; }
  .contact--email span, .contact--web span { margin-top: 11px; }

  .divider {
    position: absolute; top: 62px;
    width: 2px; height: 34px;
    background: var(--orange);
  }
  .divider--a { left: 319px; }
  .divider--b { left: 537px; }

  .card__band {
    position: absolute; left: 0; right: 0; bottom: 0;
    height: 55px; background: var(--orange);
  }
</style>
</head>
<body>
<main class="canvas">

  <section class="card card--front" aria-label="Card front">
    <div class="brand">
      <div class="brand__dot"></div>
      <div class="brand__name">Korvan Fuels</div>
    </div>
  </section>

  <section class="card card--back" aria-label="Card back">
    <div class="name-tag">
      <div class="name-tag__name"><strong>Peter</strong> Morrow</div>
      <div class="name-tag__role">Director</div>
    </div>

    <div class="contacts">
      <div class="contact contact--email">
        <svg viewBox="0 0 40 40" fill="none" stroke="#f58a33" stroke-width="1.6" aria-hidden="true">
          <rect x="5" y="10" width="30" height="20"/>
          <path d="M5 10 L20 22 L35 10"/>
        </svg>
        <span>pmorrow@korvanse.com.au</span>
      </div>
      <div class="contact contact--web">
        <svg viewBox="0 0 40 40" fill="none" stroke="#f58a33" stroke-width="1.6" aria-hidden="true">
          <circle cx="20" cy="20" r="16"/>
          <ellipse cx="20" cy="20" rx="7" ry="16"/>
          <path d="M4 20 H36 M7 12 H33 M7 28 H33 M20 4 V36"/>
        </svg>
        <span>www.korvanse.com.au</span>
      </div>
      <div class="contact contact--post">
        <svg viewBox="0 0 40 40" fill="none" stroke="#f58a33" stroke-width="1.6" aria-hidden="true">
          <path d="M4 21 L20 6 L36 21"/>
          <path d="M9 17 V35 H31 V17"/>
          <rect x="16" y="24" width="8" height="11"/>
        </svg>
        <span>PO Box 347, Marlow Vale<br>NSW, 2790</span>
      </div>
      <div class="divider divider--a"></div>
      <div class="divider divider--b"></div>
    </div>

    <div class="card__band"></div>
  </section>

</main>
</body>
</html>
```